Broadcaster,Conference Host,Facilitator

Looking for a business card and logo to create the Grant Felber brand .. Something with a slant towards radio and conference speaking
I like the idea of classic black white or grey but open to suggestions

Target Market(s)

Corporates

Industry/Entity Type

Business

Contact Information for Business Card

Grant Felber
Email : Grant.Felber@quorvamail.co.uk
Mobile : +44 7700 382046
Twitter : @Grantfelber

Font styles to use
Serif
Decorative
Script

Requirements
Must have
• Feel classy and dynamic
Should not have
• Cartoons

```html
<!DOCTYPE html>
<html lang="en">
<head>
<meta charset="utf-8">
<title>Grant Felber — Logo and Business Card</title>
<link rel="stylesheet" href="https://fonts.googleapis.com/css2?family=Cinzel:wght@500&family=Raleway:wght@400;700&display=swap">
<style>
  :root {
    --white: #ffffff;
    --grey: #7f7f84;
    --teal: #6fcbcc;
    --blue-light: #1b8fd0;
    --blue-dark: #0d6fae;
    --wordmark-font: "Cinzel", serif;
    --body-font: "Raleway", sans-serif;
  }
  * { margin: 0; padding: 0; box-sizing: border-box; }
  html, body { width: 1200px; height: 1200px; overflow: hidden; background: var(--white); }
  .board { position: relative; width: 1200px; height: 1200px; background: var(--white); }

  .wordmark {
    position: absolute;
    display: flex; align-items: center; gap: 16px;
    font-family: var(--wordmark-font); font-weight: 500;
    color: var(--grey); white-space: nowrap; letter-spacing: 2px;
  }
  .wordmark-square { background: var(--teal); flex: none; }

  .hero-wordmark { left: 0; width: 1200px; top: 230px; justify-content: center; font-size: 84px; }
  .hero-wordmark .wordmark-square { width: 30px; height: 30px; }

  .backdrop {
    position: absolute; left: 0; top: 402px; width: 1200px; height: 673px;
    background: linear-gradient(160deg, var(--blue-light) 0%, #1784c6 50%, var(--blue-dark) 100%);
  }

  .card { position: absolute; left: 350px; width: 571px; height: 324px; background: var(--white); overflow: hidden; }
  .card-front { top: 402px; height: 327px; }
  .card-back { top: 751px; }

  .stripe-grey { position: absolute; left: 0; width: 100%; height: 10px; background: var(--grey); }
  .stripe-teal { position: absolute; left: 0; width: 100%; background: var(--teal); }
  .card-front .stripe-grey { top: 277px; }
  .card-front .stripe-teal { top: 298px; height: 29px; }
  .card-back .stripe-grey { top: 275px; }
  .card-back .stripe-teal { top: 296px; height: 28px; }

  .card-wordmark { left: 0; width: 100%; top: 122px; justify-content: center; font-size: 46px; gap: 10px; }
  .card-wordmark .wordmark-square { width: 18px; height: 18px; }

  .name-block {
    position: absolute; left: 37px; top: 0; width: 187px; height: 125px;
    background: var(--teal); color: var(--white);
    font-family: var(--body-font); font-weight: 700; font-size: 19px;
    display: flex; align-items: flex-end; padding: 0 0 7px 8px; white-space: nowrap;
  }

  .contact-list { position: absolute; left: 266px; top: 68px; list-style: none; }
  .contact-item {
    display: flex; align-items: center; gap: 12px; height: 22px; margin-bottom: 34px;
    font-family: var(--body-font); font-size: 17px; color: var(--grey); white-space: nowrap;
  }
  .contact-item:nth-child(2) { margin-bottom: 23px; }
  .contact-icon { width: 26px; height: 22px; flex: none; }
  .handle-dot { width: 20px; height: 20px; border-radius: 50%; background: var(--teal); margin: 0 3px; flex: none; }

  .back-wordmark { right: 26px; top: 222px; font-size: 20px; gap: 8px; letter-spacing: 1px; }
  .back-wordmark .wordmark-square { width: 10px; height: 10px; }
</style>
</head>
<body>
<main class="board">
  <div class="wordmark hero-wordmark"><span class="wordmark-square"></span>Grant Felber</div>

  <div class="backdrop"></div>

  <section class="card card-front">
    <div class="wordmark card-wordmark"><span class="wordmark-square"></span>Grant Felber</div>
    <div class="stripe-grey"></div>
    <div class="stripe-teal"></div>
  </section>

  <section class="card card-back">
    <div class="name-block">GRANT FELBER</div>
    <ul class="contact-list">
      <li class="contact-item">
        <svg class="contact-icon" viewBox="0 0 26 22" aria-hidden="true">
          <rect x="2" y="4" width="22" height="14" fill="var(--teal)"/>
          <path d="M2 4 L13 12 L24 4 M2 18 L10 10 M24 18 L16 10" stroke="var(--white)" stroke-width="1.6" fill="none"/>
        </svg>
        Grant.Felber@quorvamail.co.uk
      </li>
      <li class="contact-item">
        <svg class="contact-icon" viewBox="0 0 26 22" aria-hidden="true">
          <path d="M6 1 C4 1 2 3 2 6 C3 13 9 19 17 21 C20 21 22 19 22 17 L18 13 L15 15 C12 14 9 11 8 8 L10 5 Z" fill="var(--teal)"/>
        </svg>
        +44 7700 382046
      </li>
      <li class="contact-item">
        <span class="handle-dot"></span>
        @Grantfelber
      </li>
    </ul>
    <div class="wordmark back-wordmark"><span class="wordmark-square"></span>Grant Felber</div>
    <div class="stripe-grey"></div>
    <div class="stripe-teal"></div>
  </section>
</main>
</body>
</html>
```